Architectural Design practice needs new logo /letterhead design

We need a new logo / letterhead design to freshen up the practice image. We are an architects practice working in all building design sectors and want a new modern fresh logo / letterhead but retaining a professional feel, so not too gimmicky. The current branding colour palette uses blue and grey, which we still like, but we are also open to other suggestions. I have attached our current letterhead which has served us well and incorporates the FENC logo, but this was produced in-house using only Word when we first started the business and we would now like a new more modern and professional design.
Possibly include the acronym KPT , or kpt, second file added shows an attempt I did myself, which is a bit basic but gives an idea of the type of thing we are looking for

File added showing the type of thing we are looking for

Building

Sans Serif

```html
<!DOCTYPE html>
<html lang="en">
<head>
<meta charset="utf-8">
<title>K Porter Chartered Architects – Stationery</title>
<link rel="stylesheet" href="https://fonts.googleapis.com/css2?family=Jost:ital,wght@0,400;0,500;0,600;1,400&family=Bodoni+Moda:wght@400&display=swap">
<style>
  :root {
    --brand-blue: #4a74a0;
    --ink: #111111;
    --paper: #ffffff;
    --backdrop: #efefef;
    --shadow: rgba(0, 0, 0, 0.22);
  }
  * { box-sizing: border-box; margin: 0; padding: 0; }
  html, body { width: 1200px; height: 848px; overflow: hidden; }
  body {
    background: var(--backdrop);
    font-family: "Jost", sans-serif;
    color: var(--ink);
    position: relative;
  }

  /* Brand lockup */
  .lockup { position: absolute; display: flex; flex-direction: column; align-items: center; color: var(--brand-blue); font-weight: 600; }
  .lockup__mark { background: var(--brand-blue); }
  .lockup__name { letter-spacing: 0.08em; line-height: 1; }
  .lockup__tagline { letter-spacing: 0.06em; line-height: 1; }

  .lockup--hero { left: 131px; top: 78px; width: 319px; }
  .lockup--hero .lockup__mark { width: 96px; height: 96px; margin-bottom: 38px; }
  .lockup--hero .lockup__name { font-size: 56px; }
  .lockup--hero .lockup__tagline { font-size: 20px; margin-top: 18px; }

  /* Business cards */
  .card {
    position: absolute; left: 125px; width: 405px; height: 195px;
    background: var(--paper);
    box-shadow: 0 1px 6px var(--shadow);
  }
  .card--front { top: 375px; }
  .card--back { top: 590px; }

  .card--front .lockup { left: 0; right: 0; top: 48px; }
  .card--front .lockup__mark { width: 40px; height: 40px; margin-bottom: 16px; }
  .card--front .lockup__name { font-size: 30px; }
  .card--front .lockup__tagline { font-size: 11px; margin-top: 8px; }

  .card__holder { position: absolute; left: 20px; top: 20px; font-style: italic; font-size: 14px; letter-spacing: 0.03em; }
  .card__dash { position: absolute; left: 23px; top: 44px; width: 9px; height: 2px; background: var(--ink); }
  .card__role { position: absolute; left: 20px; top: 52px; font-size: 14px; font-weight: 600; letter-spacing: 0.04em; }
  .card__rule { position: absolute; left: 17px; top: 77px; width: 328px; height: 1px; background: var(--ink); }
  .card__contact { position: absolute; left: 15px; font-style: italic; font-size: 14px; letter-spacing: 0.03em; }
  .card__contact--tel { top: 90px; }
  .card__contact--email { top: 125px; }
  .card__contact--fax { top: 162px; }

  .card--back .lockup { right: 14px; top: 134px; }
  .card--back .lockup__mark { width: 14px; height: 14px; margin-bottom: 6px; }
  .card--back .lockup__name { font-size: 15px; }
  .card--back .lockup__tagline { font-size: 6.5px; margin-top: 3px; }

  /* Letterhead */
  .letterhead {
    position: absolute; left: 712px; top: 161px; width: 403px; height: 580px;
    background: var(--paper);
    box-shadow: 0 1px 6px var(--shadow);
  }
  .letterhead .lockup { left: 0; right: 0; top: 32px; }
  .letterhead .lockup__mark { width: 22px; height: 22px; margin-bottom: 8px; }
  .letterhead .lockup__name { font-size: 18px; }
  .letterhead .lockup__tagline { font-size: 7.5px; margin-top: 4px; }

  .letterhead__address {
    position: absolute; left: 281px; top: 124px;
    font-size: 8px; font-weight: 600; line-height: 10px; letter-spacing: 0.06em;
  }
  .letterhead__salutation { position: absolute; left: 22px; top: 218px; font-size: 8.5px; font-weight: 600; letter-spacing: 0.03em; }
  .letterhead__body {
    position: absolute; left: 22px; top: 250px; width: 363px;
    font-family: "Bodoni Moda", serif; font-size: 8.5px; line-height: 10.5px;
  }
  .letterhead__body p + p { margin-top: 12px; }
  .letterhead__band {
    position: absolute; left: 0; right: 0; bottom: 0; height: 93px;
    background: var(--brand-blue);
  }
</style>
</head>
<body>

  <div class="lockup lockup--hero">
    <div class="lockup__mark"></div>
    <div class="lockup__name">K PORTER</div>
    <div class="lockup__tagline">CHARTERED ARCHITECTS</div>
  </div>

  <section class="card card--front">
    <div class="lockup">
      <div class="lockup__mark"></div>
      <div class="lockup__name">K PORTER</div>
      <div class="lockup__tagline">CHARTERED ARCHITECTS</div>
    </div>
  </section>

  <section class="card card--back">
    <div class="card__holder">MR. LOREM IPSUM</div>
    <div class="card__dash"></div>
    <div class="card__role">SALES ADVISOR</div>
    <div class="card__rule"></div>
    <div class="card__contact card__contact--tel">TEL :</div>
    <div class="card__contact card__contact--email">E-MAIL :</div>
    <div class="card__contact card__contact--fax">FAX :</div>
    <div class="lockup">
      <div class="lockup__mark"></div>
      <div class="lockup__name">K PORTER</div>
      <div class="lockup__tagline">CHARTERED ARCHITECTS</div>
    </div>
  </section>

  <section class="letterhead">
    <div class="lockup">
      <div class="lockup__mark"></div>
      <div class="lockup__name">K PORTER</div>
      <div class="lockup__tagline">CHARTERED ARCHITECTS</div>
    </div>
    <address class="letterhead__address" style="font-style: normal;">
      14 SAMPLE LANE<br>EXETER<br>UK<br>EX2 7QT
    </address>
    <div class="letterhead__salutation">Dear Sir/Madam,</div>
    <div class="letterhead__body">
      <p>Thank you for your recent enquiry regarding our services. We are an architectural practice working across all building sectors, from private homes and schools to offices, retail units and community spaces. Our team offers full design support from early sketches and planning applications through to detailed drawings, tender packages and site inspection until the day of handover.</p>
      <p>Please find enclosed a brief outline of our fees together with examples of recent work. We would be delighted to arrange a meeting at your convenience to discuss the project in more detail and walk through the site with you. We look forward to hearing from you soon.</p>
    </div>
    <div class="letterhead__band" role="img" aria-label="Blue block pattern footer band"></div>
  </section>

</body>
</html>
```